Business Card design for shipping company 'FERNHOLT INTERNATIONAL LTD'

Classic / traditional business card in black Garamond / Times New Roman or similar text for a shipping / marine transport company, containing the following information:

QUOTE

FERNHOLT INTERNATIONAL LTD

MARTIN QUESTEDGE FICS

T: +44 7902 615370
E: cargo@fernholt-example.com

UNQUOTE

Target Market(s)

Marine / Shipping industry

Contact Information for Business Card

FERNHOLT INTERNATIONAL LTD MARTIN QUESTEDGE FICS T: +44 7902 615370 E: cargo@fernholt-example.com

Font styles to use
Serif

Colors

Designer to choose colors to be used in the design.

Requirements
Must have
• Garamond / Times New Roman or similar text in black colour

```html
<!DOCTYPE html>
<html lang="en">
<head>
<meta charset="utf-8">
<title>Fernholt International Ltd – Business Card</title>
<link href="https://fonts.googleapis.com/css2?family=Cinzel:wght@400&family=Playfair+Display:wght@400&display=swap" rel="stylesheet">
<style>
  :root {
    --backdrop: #1c1c1e;
    --card: #121213;
    --card-edge: #1a1a1b;
    --ink-light: #ecebe8;
    --ink-soft: #c9c8c4;
    --rule: #8d8c89;
    --pattern-a: #151516;
    --pattern-b: #0d0d0e;
  }
  * { box-sizing: border-box; margin: 0; padding: 0; }
  html, body {
    width: 1200px;
    height: 852px;
    overflow: hidden;
    background: var(--backdrop);
  }
  .canvas {
    width: 1200px;
    height: 852px;
    display: flex;
    flex-direction: column;
    align-items: center;
    justify-content: center;
    gap: 60px;
  }
  .card {
    position: relative;
    width: 560px;
    height: 320px;
    border-radius: 22px;
    background: var(--card);
    box-shadow: inset 0 0 0 1px var(--card-edge);
    overflow: hidden;
  }
  .card-front__pattern {
    position: absolute;
    inset: 0;
    background: linear-gradient(160deg, var(--pattern-a), var(--pattern-b));
  }
  .brand {
    font-family: "Cinzel", "Times New Roman", serif;
    font-weight: 400;
    color: var(--ink-light);
    text-align: center;
    line-height: 1;
  }
  .brand__name { display: block; letter-spacing: 0.04em; }
  .brand__suffix { display: block; letter-spacing: 0.55em; }
  .card-front .brand {
    position: absolute;
    left: 0; right: 0;
    top: 50%;
    transform: translateY(-50%);
  }
  .card-front .brand__name { font-size: 52px; }
  .card-front .brand__suffix { font-size: 11px; margin-top: 4px; padding-left: 0.55em; }

  .card-back { display: flex; align-items: center; }
  .card-back .brand {
    position: absolute;
    left: 40px;
    top: 176px;
  }
  .card-back .brand__name { font-size: 30px; }
  .card-back .brand__suffix { font-size: 7px; margin-top: 3px; padding-left: 0.55em; }
  .card-back__rule {
    position: absolute;
    left: 292px;
    top: 70px;
    width: 1px;
    height: 150px;
    background: linear-gradient(var(--card), var(--rule) 30%, var(--rule) 70%, var(--card));
  }
  .contact {
    position: absolute;
    left: 308px;
    top: 100px;
    font-family: "Playfair Display", "Times New Roman", serif;
    color: var(--ink-soft);
  }
  .contact__name {
    font-size: 19px;
    color: var(--ink-light);
    margin-bottom: 10px;
  }
  .contact__line { font-size: 12.5px; line-height: 1.6; }
</style>
</head>
<body>
  <main class="canvas">
    <section class="card card-front">
      <div class="card-front__pattern" role="img" aria-label="Embossed wavy line pattern across the card face"></div>
      <div class="brand">
        <span class="brand__name">FERNHOLT</span>
        <span class="brand__suffix">INTERNATIONAL LTD</span>
      </div>
    </section>

    <section class="card card-back">
      <div class="brand">
        <span class="brand__name">FERNHOLT</span>
        <span class="brand__suffix">INTERNATIONAL LTD</span>
      </div>
      <div class="card-back__rule"></div>
      <div class="contact">
        <p class="contact__name">Martin Questedge Fics</p>
        <p class="contact__line">T: +44 7902 615370</p>
        <p class="contact__line">E: cargo@fernholt-example.com</p>
      </div>
    </section>
  </main>
</body>
</html>
```